依頼詳細
既存サイトのデザインが古くなったため、リニューアルを行います。
ワイヤーフレーム有。
参考サイト有。
https://www.morisuzu-web.jp/
今風でシンプルなデザインをお願いいたします。
メインカラーは緑で、現在のロゴをお渡ししますので、トレースしSVGで作ってください。
サイトURL
ページ数
1ページ
希望イメージ
シンプル 複雑
単色 カラフル
暗い 明るい
日常 高級
遊び心 厳粛
未来的 伝統的
女性的 男性的
希望する色
緑系
納品ファイル
• イラストレーター形式 (.ai)
補足説明
TOPページ(PC版とスマホ版)のみご提案ください。
採用した場合は、アーカイブと詳細ページ(スタイルガイド)のデザインもお願いいたします。
ワイヤーフレームではなく、サイトマップ有です。
締め切りを10日後に変更しました。
URLの記載があるのは、参考サイトです。
会社名はダミー(株式会社ダミーリサイクル)とし、
添付のサイトマップに合わせて作っていただけると幸いです。
記載内容がややこしくて申し訳ございません。
その他文言等もダミーで結構です。
よろしくお願いいたします。
■ 選んだ理由

シンプルかつ、今風なレイアウトで好感が持てました。

■ 提案者全員のお礼・コメント

修正依頼にも迅速に対応いただき、ありがとうございました。
またご提案よろしくお願いいたします。

```html
<!DOCTYPE html>
<html lang="ja">
<head>
<meta charset="utf-8">
<title>株式会社ダミーリサイクル</title>
<link href="https://fonts.googleapis.com/css2?family=Noto+Sans+JP:wght@400;500;700&display=swap" rel="stylesheet">
<style>
:root{
  --green:#45b08c;
  --green-dark:#2f9a77;
  --ink:#333333;
  --muted:#777777;
  --line:#dddddd;
  --paper:#ffffff;
  --gray-bg:#eeeeee;
  --dark:#2b2b2b;
}
*{box-sizing:border-box;margin:0;padding:0}
html,body{width:1200px;height:3076px;overflow:hidden}
body{font-family:"Noto Sans JP",sans-serif;color:var(--ink);background:var(--paper);position:relative}
.abs{position:absolute}
.photo{position:absolute}
/* header */
.site-header{position:absolute;top:0;left:0;width:1200px;height:92px;background:var(--paper)}
.brand{position:absolute;left:172px;top:15px;font-size:22px;font-weight:700;line-height:30px}
.header-tel{position:absolute;left:722px;top:8px}
.header-tel .num{font-size:24px;font-weight:700;display:flex;align-items:center;gap:8px}
.header-tel .hours{font-size:10px;color:var(--muted);margin-left:30px}
.global-nav{position:absolute;left:170px;top:62px;display:flex;font-size:12px}
.global-nav a{color:var(--ink);text-decoration:none;width:128px;border-left:1px solid var(--line);padding-left:16px;line-height:22px}
.global-nav a:last-child{border-right:1px solid var(--line)}
.contact-pill{position:absolute;left:910px;top:62px;width:118px;height:24px;border-radius:12px;background:var(--dark);color:#fff;font-size:12px;display:flex;align-items:center;justify-content:center;gap:6px}
/* hero */
.hero{position:absolute;top:92px;left:0;width:1200px;height:396px;background:linear-gradient(180deg,#3f74b8 0%,#7fa6d4 45%,#c9c6bd 75%,#a39c8f 100%)}
.hero-copy{position:absolute;left:120px;top:130px;color:#fff}
.hero-copy h1{font-size:34px;font-weight:700;letter-spacing:2px;margin-bottom:26px}
.hero-copy p{font-size:19px;font-weight:500;line-height:1.7}
/* news */
.news{position:absolute;top:520px;left:170px;width:860px;height:44px;border:1px solid var(--line);display:flex;align-items:center;font-size:12px}
.news-label{background:var(--dark);color:#fff;width:86px;height:100%;display:flex;align-items:center;justify-content:center;font-weight:500}
.news-date{color:var(--muted);margin:0 28px}
.news-title{flex:1}
.news-more{margin-right:18px;display:flex;align-items:center;gap:6px}
/* section headings */
.sec-title{position:absolute;left:0;width:1200px;text-align:center;font-size:26px;font-weight:700}
.sec-title::after{content:"";display:block;width:50px;height:4px;background:var(--green);margin:18px auto 0}
/* company */
.company-bg{position:absolute;top:720px;left:0;width:760px;height:312px;background:var(--gray-bg)}
.company-text{position:absolute;top:784px;left:172px;width:380px}
.company-text h3{font-size:16px;font-weight:700;margin-bottom:18px}
.company-text p{font-size:11px;line-height:1.9;color:var(--muted)}
.btn{display:inline-flex;align-items:center;justify-content:center;gap:8px;width:112px;height:32px;border:1px solid #999;border-radius:16px;background:#fff;font-size:11px;color:var(--ink)}
.company-text .btn{margin-top:24px}
/* services */
.service-band{position:absolute;top:1320px;left:0;width:1200px;height:440px;background:var(--green)}
.service-card{position:absolute;top:1184px;width:268px;height:496px;background:#fff}
.service-card .photo{left:0;top:0;width:268px;height:264px}
.service-card .body{position:absolute;top:284px;left:22px;right:22px}
.service-card h4{font-size:15px;font-weight:700;margin-bottom:10px}
.service-card p{font-size:11px;line-height:1.8;color:var(--muted)}
.service-card .btn{position:absolute;right:22px;bottom:22px}
/* products */
.product-card{position:absolute;top:1908px;width:268px;height:352px;background:#f1f1f1}
.product-card .photo{left:0;top:0;width:268px;height:196px;background:linear-gradient(135deg,#8e8e8e,#5d5d5d 50%,#9a9a9a)}
.product-card .body{position:absolute;top:212px;left:22px;right:22px}
.product-card h4{font-size:14px;font-weight:700;margin-bottom:10px}
.product-card h4::before{content:"■ ";color:var(--green)}
.product-card p{font-size:11px;line-height:1.8;color:var(--muted)}
/* tiles */
.tile{position:absolute;top:2400px;width:400px;height:200px}
.tile span{position:absolute;left:0;right:0;top:82px;text-align:center;color:#fff;font-size:22px;font-weight:700;letter-spacing:2px}
/* contact */
.contact{position:absolute;top:2656px;left:0;width:1200px;text-align:center}
.contact h2{font-size:22px;font-weight:700}
.contact h2::after{content:"";display:block;width:40px;height:3px;background:var(--green);margin:12px auto 0}
.contact .co{font-size:14px;font-weight:700;margin-top:18px}
.contact .addr{font-size:11px;color:var(--muted);margin-top:6px}
.contact .tel{font-size:26px;font-weight:700;margin-top:16px;display:flex;justify-content:center;align-items:center;gap:8px}
.contact .hrs{font-size:11px;color:var(--muted)}
.mail-btn{display:inline-flex;align-items:center;gap:10px;margin-top:14px;width:380px;height:42px;justify-content:center;border-radius:21px;background:var(--dark);color:#fff;font-size:13px}
/* footer */
.footer-nav{position:absolute;top:2960px;left:0;width:1200px;height:72px;background:var(--green);display:flex;justify-content:center;align-items:center;font-size:11px;color:#fff}
.footer-nav a{color:#fff;text-decoration:none;padding:0 22px;border-left:1px solid rgba(255,255,255,.6)}
.footer-nav a:last-child{border-right:1px solid rgba(255,255,255,.6)}
.to-top{position:absolute;top:2944px;left:1000px;width:32px;height:32px;border-radius:50%;background:#fff;border:1px solid var(--line);display:flex;align-items:center;justify-content:center}
.footer-bottom{position:absolute;top:3032px;left:0;width:1200px;height:44px;background:var(--green-dark);color:#fff;font-size:10px}
.footer-bottom .links{position:absolute;left:170px;top:15px;display:flex;gap:24px}
.footer-bottom .copy{position:absolute;right:170px;top:15px}
</style>
</head>
<body>

<header class="site-header">
  <div class="brand">株式会社ダミーリサイクル</div>
  <div class="header-tel">
    <div class="num"><svg width="20" height="20" viewBox="0 0 24 24"><path d="M6.6 10.8a15 15 0 0 0 6.6 6.6l2.2-2.2c.3-.3.7-.4 1-.2 1.1.4 2.3.6 3.6.6.6 0 1 .4 1 1V20c0 .6-.4 1-1 1C10.6 21 3 13.4 3 4c0-.6.4-1 1-1h3.5c.6 0 1 .4 1 1 0 1.3.2 2.5.6 3.6.1.3 0 .7-.2 1z" fill="#333"/></svg>00-0000-0000</div>
    <div class="hours">受付時間 平日9:00〜17:00</div>
  </div>
  <nav class="global-nav">
    <a>会社情報</a><a>事業紹介</a><a>商品情報</a><a>採用情報</a>
  </nav>
  <div class="contact-pill"><svg width="12" height="10" viewBox="0 0 24 18"><rect x="1" y="1" width="22" height="16" fill="none" stroke="#fff" stroke-width="2"/><path d="M1 1l11 9 11-9" fill="none" stroke="#fff" stroke-width="2"/></svg>お問い合わせ</div>
</header>

<section class="hero" role="img" aria-label="青空の下で砂利を運ぶ重機の写真">
  <div class="hero-copy">
    <h1>ハイクオリティーの追求</h1>
    <p>地球環境を考えた循環型社会の<br>形成をめざします</p>
  </div>
</section>

<div class="news">
  <div class="news-label">News</div>
  <span class="news-date">2019.00.00</span>
  <span class="news-title">ウェブサイトをリニューアルしました。</span>
  <span class="news-more">一覧を見る <svg width="12" height="8" viewBox="0 0 12 8"><path d="M0 4h11M8 1l3 3-3 3" fill="none" stroke="#333"/></svg></span>
</div>

<h2 class="sec-title" style="top:636px">会社情報</h2>
<div class="company-bg"></div>
<div class="company-text">
  <h3>株式会社ダミーリサイクルについて</h3>
  <p>ここにダミーテキストが入ります。ここにダミーテキストが入ります。ここにダミーテキストが入ります。ここにダミーテキストが入ります。ここにダミーテキストが入ります。ここにダミーテキストが入ります。ここにダミーテキストが入ります。</p>
  <span class="btn">詳細を見る <svg width="12" height="8" viewBox="0 0 12 8"><path d="M0 4h11M8 1l3 3-3 3" fill="none" stroke="#333"/></svg></span>
</div>
<div class="photo" style="top:720px;left:608px;width:592px;height:312px;background:linear-gradient(180deg,#5b8fd0,#a9c6e6 55%,#8a8f80)" role="img" aria-label="青空とガラス張りのオフィスビルの写真"></div>

<h2 class="sec-title" style="top:1104px">事業紹介</h2>
<div class="service-band"></div>
<article class="service-card" style="left:172px">
  <div class="photo" style="background:linear-gradient(135deg,#6fa34a,#2f5a24)" role="img" aria-label="若葉の芽を手で包む写真"></div>
  <div class="body"><h4>環境事業</h4><p>ここにダミーテキストが入ります。ここにダミーテキストが入ります。ここにダミーテキストが入ります。</p></div>
  <span class="btn">詳細を見る <svg width="12" height="8" viewBox="0 0 12 8"><path d="M0 4h11M8 1l3 3-3 3" fill="none" stroke="#333"/></svg></span>
</article>
<article class="service-card" style="left:466px">
  <div class="photo" style="background:linear-gradient(180deg,#c79a6d,#7a6a5c 60%,#4d4d52)" role="img" aria-label="夕暮れの道路を走るトラックの写真"></div>
  <div class="body"><h4>運搬事業</h4><p>ここにダミーテキストが入ります。ここにダミーテキストが入ります。ここにダミーテキストが入ります。</p></div>
  <span class="btn">詳細を見る <svg width="12" height="8" viewBox="0 0 12 8"><path d="M0 4h11M8 1l3 3-3 3" fill="none" stroke="#333"/></svg></span>
</article>
<article class="service-card" style="left:760px">
  <div class="photo" style="background:linear-gradient(180deg,#7fa7d6,#b9c3cc 50%,#8c8a86)" role="img" aria-label="建設現場と砂利の写真"></div>
  <div class="body"><h4>建設事業</h4><p>ここにダミーテキストが入ります。ここにダミーテキストが入ります。ここにダミーテキストが入ります。</p></div>
  <span class="btn">詳細を見る <svg width="12" height="8" viewBox="0 0 12 8"><path d="M0 4h11M8 1l3 3-3 3" fill="none" stroke="#333"/></svg></span>
</article>

<h2 class="sec-title" style="top:1804px">商品情報</h2>
<article class="product-card" style="left:172px">
  <div class="photo" role="img" aria-label="砕石の写真"></div>
  <div class="body"><h4>商品カテゴリ 01</h4><p>ここにダミーテキストが入ります。ここにダミーテキストが入ります。</p></div>
</article>
<article class="product-card" style="left:466px">
  <div class="photo" role="img" aria-label="砕石の写真"></div>
  <div class="body"><h4>商品カテゴリ 02</h4><p>ここにダミーテキストが入ります。ここにダミーテキストが入ります。</p></div>
</article>
<article class="product-card" style="left:760px">
  <div class="photo" role="img" aria-label="砕石の写真"></div>
  <div class="body"><h4>商品カテゴリ 03</h4><p>ここにダミーテキストが入ります。ここにダミーテキストが入ります。</p></div>
</article>
<span class="btn abs" style="top:2290px;left:544px">詳細を見る <svg width="12" height="8" viewBox="0 0 12 8"><path d="M0 4h11M8 1l3 3-3 3" fill="none" stroke="#333"/></svg></span>

<div class="tile" style="left:0;background:linear-gradient(135deg,#556677,#8a96a3)" role="img" aria-label="ノートパソコンで作業する手元の写真"><span>コラム</span></div>
<div class="tile" style="left:400px;background:linear-gradient(180deg,#7d96ad,#a9b8c3 60%,#6f7f76)" role="img" aria-label="風力発電の風車が並ぶ風景の写真"><span>環境保全方針</span></div>
<div class="tile" style="left:800px;background:linear-gradient(135deg,#8b8f96,#c8cdd3)" role="img" aria-label="スーツ姿の社員の写真"><span>採用情報</span></div>

<section class="contact">
  <h2>お問い合わせ</h2>
  <div class="co">株式会社ダミーリサイクル</div>
  <div class="addr">〒000-0000　〇〇県〇〇市〇〇町0-0-0</div>
  <div class="tel"><svg width="22" height="22" viewBox="0 0 24 24"><path d="M6.6 10.8a15 15 0 0 0 6.6 6.6l2.2-2.2c.3-.3.7-.4 1-.2 1.1.4 2.3.6 3.6.6.6 0 1 .4 1 1V20c0 .6-.4 1-1 1C10.6 21 3 13.4 3 4c0-.6.4-1 1-1h3.5c.6 0 1 .4 1 1 0 1.3.2 2.5.6 3.6.1.3 0 .7-.2 1z" fill="#333"/></svg>00-0000-0000</div>
  <div class="hrs">受付時間 平日9:00〜17:00</div>
  <span class="mail-btn"><svg width="16" height="12" viewBox="0 0 24 18"><rect x="1" y="1" width="22" height="16" fill="none" stroke="#fff" stroke-width="2"/><path d="M1 1l11 9 11-9" fill="none" stroke="#fff" stroke-width="2"/></svg>メールでのお問い合わせ</span>
</section>

<nav class="footer-nav">
  <a>会社情報</a><a>事業紹介</a><a>商品情報</a><a>コラム</a><a>環境保全方針</a><a>採用情報</a><a>お知らせ</a><a>お問い合わせ</a>
</nav>
<div class="to-top"><svg width="12" height="8" viewBox="0 0 12 8"><path d="M1 7l5-5 5 5" fill="none" stroke="#333" stroke-width="1.5"/></svg></div>
<footer class="footer-bottom">
  <div class="links"><span>プライバシーポリシー</span><span>サイトマップ</span></div>
  <div class="copy">© 2019 Dummy Recycle. All Rights Reserved.</div>
</footer>

</body>
</html>
```